Pinecrest Real Estate A5 Flyer

A5 Flyer for print distribution.

Front (include attached photo and branding):
Pinecrest are a new face in the Shelley & Rossmoyne real estate market. The Pinecrest team are both Shelley ‘locals’ and are genuinely and sincerely committed to this community. They put people first and pursue exceptional outcomes for their clients. This is the founding vision of Pinecrest.

Values:
Outstanding Customer Service
Timely Communication
Integrity Always
People First
Exceptional Negotiation

If you’re thinking of selling, interested in a free market appraisal, or simply want to find out more about the Pinecrest team, please reach out to Doug or Rowan for a chat. We’d love to shout you a coffee at The Lantern Coffee + Kitchen.

Pinecrest Real Estate
E: hello@pinecrestrealestate-example.com.au
W: pinecrestrealestate-example.com.au

Back (half the page about Doug, other half the page about Rowan). Please include headshots (Rowan is the younger one):

Rowan Ferrabee (Property Consultant):

Rowan has an in-depth understanding of all things property & finance related. With a degree in property & finance, diploma in finance & mortgage broking, certificate IV in real estate practice, project management roles in residential property development, plus years of small business experience as co-founder/co-owner of The Lantern Coffee + Kitchen, his experience in managing competing demands and complex scenarios runs far and wide.

Rowan also has experience in corporate negotiations which is proving to be a very beneficial skill set. Rowan is deeply committed to people and pursuing exceptional outcomes for his clients. He has built a reputation as a man of his word who is genuine and sincere and willing to go above and beyond for his clients.

rowan@pinecrestrealestate-example.com.au
0412 306 248

Doug Penberthy (Director / Licensee):

Doug has worked in various roles inclusive of being a Real Estate Agent, Bank Manager, Financial Counsellor, Mortgage Broker, and previously a Commercial Pilot. He spent eight years in remote Western Australia, where he worked for an international mining company creating strategies to help support the well-being of employees. Doug’s focus in life has always been to help people. To him, it is always about the relationship. Doug gets enormous satisfaction from seeing individuals, families, and businesses thrive financially. He has become a skilled negotiator with extensive experience working for a number of corporations and private firms.
 
What differentiates Doug is his compassion and commitment to people. He works hard to be an excellent communicator with the aim of achieving great results. He  has extensive sales experience with incredible ability to push the boundaries, think outside the box and meet or surpass expectations. This is why his clients keep coming back and continue to refer well into the future. 

doug@pinecrestrealestate-example.com.au
0438 192 607

Target Market(s)

House Sellers / House Buyers

Industry/Entity Type

Real Estate

Colors
0054AA
0677BA
7BADD7
CADEEF
E8F1F8

Requirements
Must have
• Branding / logo, river photo, head shots, company details etc
Nice to have
• Design as per attached branding guide

```html
<!DOCTYPE html>
<html lang="en">
<head>
<meta charset="utf-8">
<title>Pinecrest Real Estate – A5 Flyer</title>
<link href="https://fonts.googleapis.com/css2?family=Playfair+Display:wght@400;700;800&family=Poppins:wght@400;500;600;700&display=swap" rel="stylesheet">
<style>
  :root{
    --navy:#0c1e2c;
    --gold:#c49a6c;
    --white:#ffffff;
    --paper:#f0f0f0;
    --ink:#1b2631;
    --photo-light:#a7b2bb;
    --photo-dark:#6b7b88;
    --portrait:#d3d7db;
  }
  *{margin:0;padding:0;box-sizing:border-box}
  html,body{width:783px;height:1200px;overflow:hidden;background:var(--paper)}
  body{position:relative;font-family:"Poppins",sans-serif}
  h1,h2,h3{font-weight:inherit}
  .page{position:absolute;top:337px;width:372px;height:526px;background:var(--white);overflow:hidden;box-shadow:0 2px 8px rgba(0,0,0,.18)}
  .page--front{left:13px}
  .page--back{left:398px}
  .abs{position:absolute}
  .gold-bar{left:0;bottom:0;width:100%;height:5px;background:var(--gold)}

  /* front */
  .brand-mark{left:169px;top:33px;width:34px;height:34px;border-radius:50%;background:var(--navy)}
  .brand-name{left:0;top:74px;width:100%;padding-left:5px;text-align:center;font-family:"Playfair Display",serif;font-size:11px;line-height:1;letter-spacing:5.5px;color:var(--navy)}
  .river-photo{left:0;top:102px;width:100%;height:147px;background:linear-gradient(180deg,var(--photo-light),var(--photo-dark))}
  .front-panel{left:0;top:249px;width:100%;height:277px;background:var(--navy)}
  .frame{left:0;top:0}
  .title-top{left:0;top:252px;width:100%;text-align:center;font-family:"Playfair Display",serif;font-weight:400;font-size:25px;line-height:1;letter-spacing:-1px;color:var(--white)}
  .title-main{left:0;top:276px;width:100%;text-align:center;font-family:"Playfair Display",serif;font-weight:800;font-size:28px;line-height:1;color:var(--gold)}
  .col-head{font-family:"Playfair Display",serif;font-weight:700;font-size:9.5px;line-height:1;color:var(--white)}
  .col-head span{color:var(--gold)}
  .about-head{left:28px;top:336px}
  .about-text{left:28px;top:350px;width:143px;font-size:6px;line-height:7.4px;color:var(--white);text-align:justify}
  .river-thumb{left:28px;top:411px;width:146px;height:71px;border:1.5px solid var(--gold);border-radius:6px;background:linear-gradient(180deg,var(--photo-light),var(--photo-dark))}
  .values-head{left:206px;top:336px}
  .values{left:206px;top:347px;list-style:none}
  .values li{display:flex;align-items:center;height:17px;font-size:7px;color:var(--white)}
  .values svg{margin-right:5px;flex:none}
  .cta{left:206px;top:436px;width:140px;font-size:6px;line-height:7.4px;color:var(--white);text-align:justify}
  .footer{left:28px;top:498px;display:flex;align-items:center;gap:5px;font-size:5.4px;line-height:1;color:var(--white);white-space:nowrap}
  .footer .footer-brand{font-family:"Playfair Display",serif;font-weight:700;color:var(--gold);font-size:5.2px}
  .footer svg{vertical-align:middle;margin-right:1px}
  .page--back .footer{left:27px;top:498px;color:var(--ink)}

  /* back */
  .back-shapes{left:0;top:0}
  .headshot{border-radius:50%;border:2px solid var(--white);background:var(--portrait)}
  .headshot--rowan{left:36px;top:16px;width:104px;height:104px}
  .headshot--doug{left:237px;top:246px;width:104px;height:104px}
  .agent-name{font-family:"Playfair Display",serif;font-weight:800;font-size:19px;line-height:1;color:var(--gold);white-space:nowrap}
  .agent-role{font-weight:700;font-size:8.5px;line-height:1;text-transform:uppercase}
  .agent-line{display:flex;align-items:center;gap:4px;font-size:7.6px;line-height:1}
  .rowan-name{left:165px;top:35px}
  .rowan-role{left:165px;top:61px;color:var(--white)}
  .rowan-phone{left:165px;top:81px;color:var(--white)}
  .rowan-mail{left:165px;top:96px;color:var(--white)}
  .bio{width:323px;font-size:6.6px;line-height:8.5px;text-align:justify}
  .bio p+p{margin-top:8.5px}
  .rowan-bio{left:27px;top:138px;color:var(--white)}
  .doug-name{left:45px;top:280px}
  .doug-role{left:45px;top:303px;color:var(--navy)}
  .doug-phone{left:45px;top:320px;color:var(--ink)}
  .doug-mail{left:45px;top:335px;color:var(--ink)}
  .doug-bio{left:27px;top:366px;color:var(--ink)}
</style>
</head>
<body>

<!-- FRONT -->
<section class="page page--front">
  <div class="abs brand-mark"></div>
  <div class="abs brand-name">PINECREST</div>
  <div class="abs river-photo" role="img" aria-label="Aerial photo of the riverside suburb with the city skyline in the distance"></div>
  <div class="abs front-panel"></div>
  <svg class="abs frame" width="372" height="526" viewBox="0 0 372 526" fill="none">
    <path d="M186 22 H320 Q346 22 346 48 V318 H56 Q28 318 28 292 V282" stroke="#c49a6c" stroke-width="1.3"/>
  </svg>
  <h1 class="abs title-top">ABOUT PINECREST</h1>
  <h2 class="abs title-main">REAL ESTATE</h2>

  <h3 class="abs col-head about-head">ABOUT <span>US</span></h3>
  <p class="abs about-text">Pinecrest are a new face in the Shelley &amp; Rossmoyne real estate market. The Pinecrest team are both Shelley <b>‘locals’</b> and are genuinely and sincerely committed to this community. They put people first and pursue exceptional outcomes for their clients. This is the founding vision of Pinecrest.</p>
  <div class="abs river-thumb" role="img" aria-label="Aerial photo of the river and foreshore homes"></div>

  <h3 class="abs col-head values-head">OUR <span>VALUES</span></h3>
  <ul class="abs values">
    <li><svg width="12" height="12" viewBox="0 0 11 11"><circle cx="5.5" cy="5.5" r="5" fill="#fff" stroke="#c49a6c"/><path d="M3.3 5.6 4.9 7.1 7.8 4" stroke="#c49a6c" fill="none" stroke-width="1"/></svg>Outstanding Customer Service</li>
    <li><svg width="12" height="12" viewBox="0 0 11 11"><circle cx="5.5" cy="5.5" r="5" fill="#fff" stroke="#c49a6c"/><path d="M5.5 3v2.7l1.8 1" stroke="#c49a6c" fill="none" stroke-width="1"/></svg>Timely Communication</li>
    <li><svg width="12" height="12" viewBox="0 0 11 11"><circle cx="5.5" cy="5.5" r="5" fill="#fff" stroke="#c49a6c"/><path d="M3.3 5.6 4.9 7.1 7.8 4" stroke="#c49a6c" fill="none" stroke-width="1"/></svg>Integrity Always</li>
    <li><svg width="12" height="12" viewBox="0 0 11 11"><circle cx="5.5" cy="5.5" r="5" fill="#fff" stroke="#c49a6c"/><circle cx="5.5" cy="4.2" r="1.2" fill="#c49a6c"/><path d="M3.6 7.8Q5.5 5.4 7.4 7.8" stroke="#c49a6c" fill="none" stroke-width="1"/></svg>People First</li>
    <li><svg width="12" height="12" viewBox="0 0 11 11"><circle cx="5.5" cy="5.5" r="5" fill="#fff" stroke="#c49a6c"/><path d="M5.5 3v5" stroke="#c49a6c" stroke-width="1"/></svg>Exceptional Negotiation</li>
  </ul>
  <p class="abs cta">If you’re thinking of selling, interested in a free market appraisal, or simply want to find out more about the Pinecrest team, please reach out to Doug or Rowan for a chat. We’d love to shout you a coffee at The Lantern Coffee + Kitchen.</p>

  <div class="abs footer">
    <span class="footer-brand">PINECREST REAL ESTATE</span>
    <span><svg width="6" height="5" viewBox="0 0 6 5"><rect x=".3" y=".3" width="5.4" height="4.4" fill="#c49a6c"/><path d="M.3.3 3 2.6 5.7.3" stroke="#0c1e2c" stroke-width=".5" fill="none"/></svg> hello@pinecrestrealestate-example.com.au</span>
    <span><svg width="5" height="5" viewBox="0 0 6 6"><circle cx="3" cy="3" r="2.6" stroke="#c49a6c" fill="none" stroke-width=".6"/><path d="M.4 3h5.2M3 .4Q1.4 3 3 5.6M3 .4Q4.6 3 3 5.6" stroke="#c49a6c" fill="none" stroke-width=".5"/></svg> www.pinecrestrealestate-example.com.au</span>
  </div>
  <div class="abs gold-bar"></div>
</section>

<!-- BACK -->
<section class="page page--back">
  <svg class="abs back-shapes" width="372" height="526" viewBox="0 0 372 526" fill="none">
    <path d="M0 0H372V232H205Q192 232 184 240Q176 248 162 248H0Z" fill="#0c1e2c"/>
    <path d="M0 253H164Q178 253 186 244Q194 236 205 236" stroke="#c49a6c" stroke-width="2.5"/>
    <path d="M27 0H149V69A61 61 0 0 1 27 69Z" fill="#c49a6c"/>
    <path d="M246 30V18H338Q350 18 350 30V119H119" stroke="#c49a6c" stroke-width="1"/>
    <path d="M228 232H350V295A61 61 0 0 1 228 295Z" fill="#c49a6c"/>
    <path d="M117 273V265H39Q27 265 27 277V355H240" stroke="#c49a6c" stroke-width="1"/>
  </svg>
  <div class="abs headshot headshot--rowan" role="img" aria-label="Headshot of Rowan Ferrabee"></div>
  <div class="abs headshot headshot--doug" role="img" aria-label="Headshot of Doug Penberthy"></div>

  <h2 class="abs agent-name rowan-name">ROWAN FERRABEE</h2>
  <div class="abs agent-role rowan-role">Property Consultant</div>
  <div class="abs agent-line rowan-phone"><svg width="7" height="7" viewBox="0 0 8 8"><path d="M1.5.5 3 2 2.3 3Q3.3 4.9 5 5.7L6 5 7.5 6.5 6.6 7.5Q3.5 7.4.5 1.4Z" fill="#c49a6c"/></svg>0412 306 248</div>
  <div class="abs agent-line rowan-mail"><svg width="7" height="6" viewBox="0 0 6 5"><rect x=".3" y=".3" width="5.4" height="4.4" fill="#c49a6c"/><path d="M.3.3 3 2.6 5.7.3" stroke="#0c1e2c" stroke-width=".5" fill="none"/></svg>rowan@pinecrestrealestate-example.com.au</div>
  <div class="abs bio rowan-bio">
    <p>Rowan has an in-depth understanding of all things property &amp; finance related. With a degree in property &amp; finance, diploma in finance &amp; mortgage broking, certificate IV in real estate practice, project management roles in residential property development, plus years of small business experience as co-founder/co-owner of The Lantern Coffee + Kitchen, his experience in managing competing demands and complex scenarios runs far and wide.</p>
    <p>Rowan also has experience in corporate negotiations which is proving to be a very beneficial skill set. Rowan is deeply committed to people and pursuing exceptional outcomes for his clients. He has built a reputation as a man of his word who is genuine and sincere and willing to go above and beyond for his clients.</p>
  </div>

  <h2 class="abs agent-name doug-name">DOUG PENBERTHY</h2>
  <div class="abs agent-role doug-role">Director / Licensee</div>
  <div class="abs agent-line doug-phone"><svg width="7" height="7" viewBox="0 0 8 8"><path d="M1.5.5 3 2 2.3 3Q3.3 4.9 5 5.7L6 5 7.5 6.5 6.6 7.5Q3.5 7.4.5 1.4Z" fill="#c49a6c"/></svg>0438 192 607</div>
  <div class="abs agent-line doug-mail"><svg width="7" height="6" viewBox="0 0 6 5"><rect x=".3" y=".3" width="5.4" height="4.4" fill="#c49a6c"/><path d="M.3.3 3 2.6 5.7.3" stroke="#fff" stroke-width=".5" fill="none"/></svg>doug@pinecrestrealestate-example.com.au</div>
  <div class="abs bio doug-bio">
    <p>Doug has worked in various roles inclusive of being a Real Estate Agent, Bank Manager, Financial Counsellor, Mortgage Broker, and previously a Commercial Pilot. He spent eight years in remote Western Australia, where he worked for an international mining company creating strategies to help support the well-being of employees. Doug’s focus in life has always been to help people. To him, it is always about the relationship. Doug gets enormous satisfaction from seeing individuals, families, and businesses thrive financially. He has become a skilled negotiator with extensive experience working for a number of corporations and private firms.</p>
    <p>What differentiates Doug is his compassion and commitment to people. He works hard to be an excellent communicator with the aim of achieving great results. He has extensive sales experience with incredible ability to push the boundaries, think outside the box and meet or surpass expectations. This is why his clients keep coming back and continue to refer well into the future.</p>
  </div>

  <div class="abs footer">
    <span class="footer-brand">PINECREST REAL ESTATE</span>
    <span><svg width="6" height="5" viewBox="0 0 6 5"><rect x=".3" y=".3" width="5.4" height="4.4" fill="#c49a6c"/><path d="M.3.3 3 2.6 5.7.3" stroke="#fff" stroke-width=".5" fill="none"/></svg> hello@pinecrestrealestate-example.com.au</span>
    <span><svg width="5" height="5" viewBox="0 0 6 6"><circle cx="3" cy="3" r="2.6" stroke="#c49a6c" fill="none" stroke-width=".6"/><path d="M.4 3h5.2M3 .4Q1.4 3 3 5.6M3 .4Q4.6 3 3 5.6" stroke="#c49a6c" fill="none" stroke-width=".5"/></svg> www.pinecrestrealestate-example.com.au</span>
  </div>
  <div class="abs gold-bar"></div>
</section>

</body>
</html>
```